Conflict prevention NGO needs business cards ASAP

We are a small NGO based in New Caledonia working on conflict prevention, and will be attending a WCA-sponsored conference on small arms next month. Our work involves campaigning against the proliferation of small arms in this post-conflict South Pacific island, and we need business cards to match that purpose.
Our three basic guidelines are the following:
1. We would like the logo of our organisation (see attached) included on this card. We are open to a redesign of this logo to something more stylised or abstract.
2. The card would need to be double-sided: one side in French, the other in English. The text should ideally be minimalist, uncluttered, clear and concise. We prefer the card to visually communicate our mission. As such, we would like the card to present a central image or logo, which would give us the option of printing a texture onto that image/logo later.
3. I have attached images which might inspire the designer (bullets and the famous knotted gun statue). However, these are NOT prescriptive; they are simply thematic ideas, and designers should use their own creative license. We only ask that the overall business card communicate professionalism and a seriousness of purpose, rather than sentimentalism or idealism.
Thanks to everyone who is willing to offer up a design idea! I am grateful for your time, and look forward to viewing your ideas. I apologise, but this has to be a rush job. Please get in touch if you need further guidance.
Please note that our new website will go live on Wednesday evening (Brisbane time), in case it can provide inspiration: http://www.lagonclair.org/
Business
ENGLISH SIDE
[Name, Position] Tomas Verhalen, Director
[Organisation] The Centre for a Bright Lagoon
[Sub-Title] The first New Caledonian think tank
[Tel] +61497215304
[Email] centrelagonclair@mailvero.net
[Website] http://www.lagonclair.org/
FRENCH SIDE
[Name, Position] Tomas Verhalen, Directeur
[Organisation] Le Centre pour le Lagon Clair
[Sub-Title] Le premier pôle de réflexion calédonien
[Tel] +61497215304
*Note: We are flexible on the exact way you present the above information, and you may wish to use icons instead of "Tel." for example.

```html
<!DOCTYPE html>
<html lang="en">
<head>
<meta charset="utf-8">
<title>The Centre for a Bright Lagoon – Business Cards</title>
<link rel="stylesheet" href="https://fonts.googleapis.com/css2?family=Alfa+Slab+One&family=Archivo+Black&display=swap">
<style>
  :root {
    --backdrop: #c8915a;
    --glow: #fff3a0;
    --sky: #cfeefa;
    --sky-deep: #7fcdeb;
    --sun: #ffe93a;
    --band: #fff35c;
    --leaf: #26a83a;
    --leaf-light: #5fd06a;
    --crimson: #e4161b;
    --navy: #1b2a8f;
    --ink-white: #ffffff;
  }
  * { margin: 0; padding: 0; box-sizing: border-box; }
  html, body { width: 1200px; height: 503px; overflow: hidden; }
  body { background: var(--backdrop); position: relative; font-family: "Archivo Black", sans-serif; }

  .card {
    position: absolute;
    overflow: hidden;
    background: linear-gradient(100deg, var(--sun) 0%, var(--sky) 22%, #eef9ff 55%, #ffffff 100%);
    box-shadow: 0 0 22px 8px var(--glow);
  }
  .card--english { left: 45px; top: 13px; width: 1155px; height: 216px; }
  .card--french  { left: 100px; top: 242px; width: 1087px; height: 236px; }

  .card__sweep { position: absolute; inset: 0; width: 100%; height: 100%; }

  .card__name {
    position: absolute;
    font-family: "Alfa Slab One", serif;
    color: var(--leaf);
    font-size: 24px;
    letter-spacing: 3px;
    text-shadow: 0 0 4px #fff;
  }
  .card__role {
    position: absolute;
    font-family: "Alfa Slab One", serif;
    color: var(--crimson);
    font-size: 19px;
    letter-spacing: 1px;
  }

  .emblem {
    position: absolute;
    border-radius: 50%;
    background: radial-gradient(ellipse at center, #ffffff 0%, #d9f2fb 70%, var(--sky-deep) 100%);
    border: 2px solid rgba(40, 90, 140, 0.35);
    display: flex;
    align-items: center;
    justify-content: center;
    gap: 10px;
  }
  .emblem__dot { width: 18px; height: 18px; border-radius: 50%; background: var(--leaf); }
  .emblem__name { font-family: "Archivo Black", sans-serif; color: var(--leaf); font-size: 22px; }

  .card__title {
    position: absolute;
    left: 0; right: 0;
    text-align: center;
    font-family: "Archivo Black", sans-serif;
    color: var(--leaf-light);
    font-size: 25px;
    text-shadow: 0 0 5px #fff, 0 0 2px #fff;
  }
  .card__subtitle {
    position: absolute;
    left: 0; right: 0;
    text-align: center;
    color: var(--ink-white);
    font-family: "Alfa Slab One", serif;
    font-size: 15px;
    text-shadow: 0 0 3px #8ab;
  }

  .contact-band {
    position: absolute;
    left: 0; right: 0; bottom: 0;
    background: linear-gradient(180deg, rgba(255,243,92,0.75), var(--band));
    border-top: 2px solid #f5c400;
  }
  .card--english .contact-band { height: 58px; }
  .card--french .contact-band { height: 70px; }

  .contact-band__heading {
    position: absolute;
    font-family: "Alfa Slab One", serif;
    color: var(--navy);
    font-size: 21px;
    letter-spacing: 3px;
  }
  .contact-line {
    position: absolute;
    font-family: "Alfa Slab One", serif;
    font-size: 17px;
    letter-spacing: 1px;
    white-space: nowrap;
  }
  .contact-line__label { color: var(--navy); }
  .contact-line__value { color: var(--crimson); }
</style>
</head>
<body>

  <section class="card card--english" lang="en">
    <svg class="card__sweep" viewBox="0 0 1155 216" preserveAspectRatio="none" role="img" aria-label="Soft blue and yellow swooshing wave graphic across the card">
      <defs>
        <linearGradient id="sweepEn" x1="0" y1="0" x2="1" y2="0">
          <stop offset="0" stop-color="#ffe93a" stop-opacity="0.9"/>
          <stop offset="0.4" stop-color="#9fd9f0" stop-opacity="0.55"/>
          <stop offset="1" stop-color="#ffffff" stop-opacity="0"/>
        </linearGradient>
      </defs>
      <rect width="1155" height="216" fill="url(#sweepEn)"/>
    </svg>

    <p class="card__name" style="left:770px; top:8px;">Tomas Verhalen</p>
    <p class="card__role" style="left:880px; top:36px;">Director</p>

    <div class="emblem" style="left:345px; top:20px; width:385px; height:88px;">
      <span class="emblem__dot"></span>
      <span class="emblem__name">Bright Lagoon</span>
    </div>

    <h1 class="card__title" style="top:104px; padding-right:40px;">The Centre for a Bright Lagoon</h1>
    <p class="card__subtitle" style="top:132px; padding-right:40px;">The first New Caledonian think tank</p>

    <div class="contact-band">
      <p class="contact-band__heading" style="left:505px; top:-6px;">CONTACT</p>
      <p class="contact-line" style="left:30px; top:14px;">
        <span class="contact-line__label">Tel:</span>
        <span class="contact-line__value">+61497215304</span>
      </p>
      <p class="contact-line" style="left:455px; top:14px;">
        <span class="contact-line__label">Email:</span>
        <span class="contact-line__value">centrelagonclair@mailvero.net</span>
      </p>
      <p class="contact-line" style="left:30px; top:34px;">
        <span class="contact-line__label">Website:</span>
        <span class="contact-line__value">www.lagonclair.org</span>
      </p>
    </div>
  </section>

  <section class="card card--french" lang="fr">
    <svg class="card__sweep" viewBox="0 0 1087 236" preserveAspectRatio="none" role="img" aria-label="Vague stylisée bleue et jaune en arrière-plan de la carte">
      <defs>
        <linearGradient id="sweepFr" x1="0" y1="0" x2="1" y2="0">
          <stop offset="0" stop-color="#ffe93a" stop-opacity="0.9"/>
          <stop offset="0.4" stop-color="#9fd9f0" stop-opacity="0.55"/>
          <stop offset="1" stop-color="#ffffff" stop-opacity="0"/>
        </linearGradient>
      </defs>
      <rect width="1087" height="236" fill="url(#sweepFr)"/>
    </svg>

    <p class="card__name" style="left:790px; top:10px;">Tomas Verhalen</p>
    <p class="card__role" style="left:880px; top:36px;">Directeur</p>

    <div class="emblem" style="left:336px; top:16px; width:436px; height:86px;">
      <span class="emblem__dot"></span>
      <span class="emblem__name">Lagon Clair</span>
    </div>

    <h1 class="card__title" style="top:102px; padding-right:80px;">Le Centre pour le Lagon Clair</h1>

    <div class="contact-band">
      <p class="contact-band__heading" style="left:430px; top:-4px;">CONTACT</p>
      <p class="contact-line" style="left:15px; top:20px;">
        <span class="contact-line__label">Tel:</span>
        <span class="contact-line__value">+61497215304</span>
      </p>
      <p class="contact-line" style="left:420px; top:20px;">
        <span class="contact-line__label">Email:</span>
        <span class="contact-line__value">centrelagonclair@mailvero.net</span>
      </p>
      <p class="contact-line" style="left:15px; top:42px;">
        <span class="contact-line__label">Website:</span>
        <span class="contact-line__value">www.lagonclair.org</span>
      </p>
    </div>
  </section>

</body>
</html>
```